Creative Website for Start Up in Italy

We need a wordpress design for a new start up based in Italy called "DoRuVi". Our start up takes a human-centered, design-based approach to help organizations in the public and private sectors innovate and grow. Through Participatory design we try to actively involve all stakeholders (e.g. employees, partners, customers, citizens, end users) in the design process to help ensure the final result meets their needs and is usable. The final design should recall our logo (see attachment) and should have the following setting: Home - Mission - About Us - What we Do - Portfolio - Blog - Contact Us. Moreover we would like a Responsive Multi-language, cross browser compatible, mobile ready website with a back office. Note that the designer should also do the implementation, meaning that we need a full website (including CSS and XHTML) as we already have a web hosting www.doruvi.it and a blog doruviblog.example-host.com

```html
<!DOCTYPE html>
<html lang="en">
<head>
<meta charset="utf-8">
<title>DoRuVi – Be Part Of The Solution</title>
<link href="https://fonts.googleapis.com/css2?family=Questrial&family=Arimo:wght@400;700&display=swap" rel="stylesheet">
<style>
:root{
  --green:#6cbd45;
  --blue:#0aa0e0;
  --blue-dark:#1a8fd0;
  --grey:#6b6b6b;
  --grey-light:#8a8a8a;
  --btn-grey:#76767a;
  --card-border:#d8ead0;
  --white:#ffffff;
}
*{margin:0;padding:0;box-sizing:border-box}
html,body{width:831px;height:1200px;overflow:hidden;background:var(--white)}
body{position:relative;font-family:"Questrial",sans-serif;color:var(--grey)}
.abs{position:absolute}

/* header */
.site-header{left:0;top:0;width:831px;height:89px}
.brand-mark{left:82px;top:30px;width:12px;height:12px;border-radius:50%;background:var(--green)}
.brand-divider{left:175px;top:20px;width:1px;height:46px;background:#9a9a9a}
.brand-name{left:184px;top:18px;font-size:32px;color:var(--grey);line-height:1}
.brand-tagline{left:185px;top:52px;font-size:10px;color:var(--grey-light);letter-spacing:.3px}
.main-nav{right:80px;top:53px;font-size:10px;display:flex;gap:7px;color:var(--grey)}
.main-nav .sep{color:var(--grey-light)}
.main-nav .active{color:var(--blue)}

/* hero */
.hero{left:0;top:89px;width:831px;height:384px}
.hero-title{left:94px;top:140px;font-size:30px;color:#7a7a7a}
.hero-tagline{left:138px;top:176px;font-size:17px;color:var(--blue-dark)}
.hero-heading{left:91px;top:196px;font-size:56px;color:var(--white);letter-spacing:1px}
.hero-button{left:94px;top:281px;width:171px;height:34px;background:var(--btn-grey);color:var(--white);font-size:21px;line-height:34px;text-align:center;border-radius:2px}
.intro-box{left:87px;top:419px;width:657px;height:117px;background:var(--blue);color:var(--white);font-size:22.5px;line-height:28px;padding:15px 16px;white-space:nowrap}

/* services */
.section-title{left:0;top:556px;width:831px;text-align:center;font-size:24px;color:var(--grey);font-weight:400}
.card{top:666px;width:195px;height:163px;border:1px solid var(--card-border);background:var(--white);text-align:center}
.card-icon{top:-45px;left:66px;width:62px;height:62px;border-radius:50%;border:2px solid var(--green);background:var(--white);border-bottom-color:transparent}
.card-title{position:absolute;top:30px;left:0;width:100%;font-size:18px;color:var(--blue-dark);font-weight:400}
.card-text{position:absolute;top:60px;left:12px;width:171px;font-family:"Arimo",sans-serif;font-size:9px;line-height:11.6px;color:var(--grey)}
.card-button{position:absolute;top:135px;left:64px;width:68px;height:18px;background:var(--green);color:var(--white);font-family:"Arimo",sans-serif;font-weight:700;font-size:8.5px;line-height:18px;border-radius:2px}

/* testimonials */
.testimonials{left:0;top:893px;width:831px;height:268px}
.testimonials-title{left:0;top:922px;width:831px;text-align:center;font-size:14px;color:var(--white);letter-spacing:.5px;font-weight:400}
.quote{left:175px;top:977px;width:492px;font-family:"Arimo",sans-serif;font-size:7.6px;line-height:11.6px;color:var(--white)}
.quote-mark{font-family:"Arimo",sans-serif;font-weight:700;font-size:14px;color:var(--white)}
.client-name{left:0;top:1102px;width:831px;text-align:center;font-family:"Arimo",sans-serif;font-weight:700;font-size:8px;color:var(--blue)}

/* footer */
.site-footer{left:0;top:1161px;width:831px;height:39px;background:var(--blue);font-family:"Arimo",sans-serif;font-size:7.5px;color:var(--white)}
.footer-nav{left:86px;top:15px;display:flex;gap:14px}
.copyright{right:92px;top:16px}
</style>
</head>
<body>

<header class="abs site-header">
  <span class="abs brand-mark"></span>
  <span class="abs brand-divider"></span>
  <span class="abs brand-name">DoRuVi</span>
  <div class="abs brand-tagline">Be Part Of The Solution</div>
  <nav class="abs main-nav">
    <span class="active">Home</span><span class="sep">/</span>
    <span>Mission</span><span class="sep">/</span>
    <span>About Us</span><span class="sep">/</span>
    <span>What we Do</span><span class="sep">/</span>
    <span>Portfolio</span><span class="sep">/</span>
    <span>Blog</span><span class="sep">/</span>
    <span>Contact</span>
  </nav>
</header>

<section class="abs hero">
  <svg width="831" height="384" viewBox="0 0 831 384">
    <defs>
      <linearGradient id="heroPhoto" x1="0" y1="0" x2="1" y2="1">
        <stop offset="0" stop-color="#d9dde4"/>
        <stop offset=".45" stop-color="#2e4a86"/>
        <stop offset="1" stop-color="#1b2238"/>
      </linearGradient>
      <linearGradient id="heroGreen" x1="0" y1="0" x2="1" y2="1">
        <stop offset="0" stop-color="#72c049"/>
        <stop offset="1" stop-color="#64b23f"/>
      </linearGradient>
    </defs>
    <rect width="831" height="384" fill="url(#heroGreen)"/>
    <polygon points="422,0 831,0 831,384 340,384" fill="url(#heroPhoto)" role="img" aria-label="Photo of two businessmen reviewing documents together"/>
  </svg>
</section>
<div class="abs hero-title">DoRuVi</div>
<div class="abs hero-tagline">Be Part of the Solution</div>
<div class="abs hero-heading">MISSION</div>
<div class="abs hero-button">More Details</div>
<div class="abs intro-box">Our start up takes a human-centered, design-based<br>approach to help organizations in the public and private<br>sectors innovate and grow...</div>

<h2 class="abs section-title">What We Do</h2>
<svg class="abs" style="left:344px;top:594px" width="142" height="10" viewBox="0 0 142 10">
  <line x1="0" y1="5" x2="60" y2="5" stroke="#9a9a9a" stroke-width="1"/>
  <line x1="82" y1="5" x2="142" y2="5" stroke="#9a9a9a" stroke-width="1"/>
  <circle cx="64" cy="5" r="1.6" fill="#6b6b6b"/><circle cx="71" cy="5" r="1.6" fill="#6b6b6b"/><circle cx="78" cy="5" r="1.6" fill="#6b6b6b"/>
</svg>

<svg class="abs" style="left:38px;top:718px" width="20" height="32" viewBox="0 0 20 32"><polyline points="16,3 4,16 16,29" fill="none" stroke="#8a8a8a" stroke-width="3"/></svg>
<svg class="abs" style="left:778px;top:718px" width="20" height="32" viewBox="0 0 20 32"><polyline points="4,3 16,16 4,29" fill="none" stroke="#8a8a8a" stroke-width="3"/></svg>

<article class="abs card" style="left:80px">
  <div class="abs card-icon">
    <svg width="58" height="58" viewBox="0 0 58 58"><circle cx="29" cy="24" r="7" fill="#3a3a3a"/><path d="M17 44 q12 -16 24 0 z" fill="#3a3a3a"/><path d="M21 24 a8 8 0 0 1 16 0" fill="none" stroke="#3a3a3a" stroke-width="1.5"/></svg>
  </div>
  <h3 class="card-title">DoRuVi Mission</h3>
  <p class="card-text">Working as Consultant Neurosurgeon in private hospitals from last 11 years, in Jalandhar, operated around 7000 cases. Performing of surgery. Brain &amp; Spinal Trauma,Brain &amp; Spine Tumours</p>
  <span class="card-button">Read more</span>
</article>
<article class="abs card" style="left:318px">
  <div class="abs card-icon">
    <svg width="58" height="58" viewBox="0 0 58 58"><path d="M18 28 a11 11 0 1 1 20 6" fill="none" stroke="#3a3a3a" stroke-width="3"/><polygon points="34,32 42,30 40,38" fill="#3a3a3a"/><text x="15" y="37" font-family="Arimo,sans-serif" font-weight="700" font-size="10" fill="#3a3a3a">ALL</text></svg>
  </div>
  <h3 class="card-title">DoRuVi Mission</h3>
  <p class="card-text">Working as Consultant Neurosurgeon in private hospitals from last 11 years, in Jalandhar, operated around 7000 cases. Performing of surgery. Brain &amp; Spinal Trauma,Brain &amp; Spine Tumours</p>
  <span class="card-button">Read more</span>
</article>
<article class="abs card" style="left:555px">
  <div class="abs card-icon">
    <svg width="58" height="58" viewBox="0 0 58 58"><rect x="19" y="15" width="20" height="26" rx="2" fill="none" stroke="#3a3a3a" stroke-width="1.8"/><rect x="25" y="12" width="8" height="5" fill="#3a3a3a"/><line x1="27" y1="23" x2="35" y2="23" stroke="#3a3a3a" stroke-width="1.5"/><line x1="27" y1="29" x2="35" y2="29" stroke="#3a3a3a" stroke-width="1.5"/><line x1="27" y1="35" x2="35" y2="35" stroke="#3a3a3a" stroke-width="1.5"/><polyline points="22,23 23.5,24.5 25,21.5" fill="none" stroke="#3a3a3a" stroke-width="1.2"/><polyline points="22,29 23.5,30.5 25,27.5" fill="none" stroke="#3a3a3a" stroke-width="1.2"/></svg>
  </div>
  <h3 class="card-title">DoRuVi Mission</h3>
  <p class="card-text">Working as Consultant Neurosurgeon in private hospitals from last 11 years, in Jalandhar, operated around 7000 cases. Performing of surgery. Brain &amp; Spinal Trauma,Brain &amp; Spine Tumours</p>
  <span class="card-button">Read more</span>
</article>

<section class="abs testimonials">
  <svg width="831" height="268" viewBox="0 0 831 268" role="img" aria-label="Dimmed photo of hands pointing at charts on a desk">
    <defs>
      <linearGradient id="testiBg" x1="0" y1="0" x2="1" y2="1">
        <stop offset="0" stop-color="#4a4f55"/>
        <stop offset=".5" stop-color="#3c4146"/>
        <stop offset="1" stop-color="#2f3d4c"/>
      </linearGradient>
    </defs>
    <rect width="831" height="268" fill="url(#testiBg)"/>
  </svg>
</section>
<svg class="abs" style="left:215px;top:928px" width="410" height="6" viewBox="0 0 410 6">
  <line x1="0" y1="3" x2="116" y2="3" stroke="#0aa0e0" stroke-width="1"/>
  <line x1="80" y1="3" x2="116" y2="3" stroke="#0aa0e0" stroke-width="3"/>
  <line x1="296" y1="3" x2="410" y2="3" stroke="#0aa0e0" stroke-width="1"/>
  <line x1="296" y1="3" x2="332" y2="3" stroke="#0aa0e0" stroke-width="3"/>
</svg>
<h2 class="abs testimonials-title">CLIENT'S&nbsp; TESTIMONIALS</h2>
<span class="abs quote-mark" style="left:169px;top:970px">"</span>
<p class="abs quote">&nbsp;&nbsp;&nbsp;&nbsp;Lorem ipsum dolor sit amet, consectetur adipisicing elit, sed do eiusmod tempor incididunt ut labore et dolore magna aliqua. Ut enim ad minim veniam, quis nostrud exercitation ullamco laboris nisi ut aliquip ex ea commodo consequat. Duis aute irure dolor in reprehenderit in voluptate velit esse cillum dolore eu fugiat nulla pariatur. Excepteur sint occaecat cupidatat non proident, sunt in culpa qui officia deserunt mollit anim id est laborum Duis aute irure dolor in reprehenderit in voluptate.</p>
<span class="abs quote-mark" style="left:525px;top:1015px">"</span>
<svg class="abs" style="left:384px;top:1034px" width="58" height="58" viewBox="0 0 58 58" role="img" aria-label="Portrait of the client">
  <circle cx="29" cy="29" r="27" fill="#8d939a" stroke="#ffffff" stroke-width="3"/>
</svg>
<div class="abs client-name">Mr Paolo Neri</div>
<svg class="abs" style="left:393px;top:1128px" width="42" height="10" viewBox="0 0 42 10">
  <circle cx="5" cy="5" r="4" fill="#6cbd45"/><circle cx="21" cy="5" r="4" fill="#ffffff"/><circle cx="37" cy="5" r="4" fill="#6cbd45"/>
</svg>

<footer class="abs site-footer">
  <nav class="abs footer-nav">
    <span>Home</span><span>|</span><span>Mission</span><span>|</span><span>About Us</span><span>|</span><span>What we Do</span><span>|</span><span>Portfolio</span><span>|</span><span>Blog</span><span>|</span><span>Contact Us</span>
  </nav>
  <div class="abs copyright">© Copyright DoRuVi. 2014, All Rights Reserved.</div>
</footer>

</body>
</html>
```